Calloway needs a modernized design

We would like a modern update (that can be responsive) to our existing website. Attached are the two existing pages we would like new concepts of - our home page and a page about one of our locations.

Calloway is provides executive offices and virtual office services. Startups, law firms, and financial services are our primary clients. We would like a professional, clean design, leaning towards minimalist. We intend to greatly reduce/eliminate the long paragraphs of text.

Industry/Entity Type

Business Service

Number of Pages Required

2 page

Requirements
Must have
• A design that can be responsive
Nice to have
• Large image(s) on home page that rotate.

```html
<!DOCTYPE html>
<html lang="en">
<head>
<meta charset="utf-8">
<title>Calloway – Request more information</title>
<link rel="stylesheet" href="https://fonts.googleapis.com/css2?family=Arimo:wght@400;500&display=swap">
<style>
  :root {
    --navy: #2b3a68;
    --white: #ffffff;
    --accent: #fff200;
    --photo-warm: #b07a55;
    --photo-cool: #c9c2b0;
    --photo-light: #d8cfb4;
  }
  * { box-sizing: border-box; margin: 0; padding: 0; }
  html, body {
    width: 990px; height: 1200px; overflow: hidden;
    background: var(--white);
    font-family: "Arimo", Arial, sans-serif;
    color: var(--navy);
  }
  .page {
    position: relative;
    width: 1000px; height: 1212px;
    transform: scale(0.99); transform-origin: 0 0;
  }
  .brand {
    position: absolute; top: 17px; left: 0; width: 1000px;
    display: flex; justify-content: center; align-items: center; gap: 10px;
  }
  .brand-rule { width: 100px; height: 9px; background: var(--navy); }
  .brand-rule.left { border-radius: 0 0 0 10px; }
  .brand-rule.right { border-radius: 0 0 10px 0; }
  .brand-name { font-size: 24px; font-weight: 500; color: var(--navy); line-height: 40px; }
  .page-title {
    position: absolute; top: 76px; left: 0; width: 1000px;
    text-align: center; font-size: 40px; font-weight: 400; color: var(--navy);
  }
  .request-form {
    position: absolute; left: 100px; top: 167px; width: 525px; height: 779px;
    border: 3px solid var(--navy); padding: 16px 17px 0 10px;
  }
  .field {
    position: relative; height: 50px; margin-bottom: 10px;
    border: 1px solid var(--navy);
    font-size: 20px; line-height: 48px; padding-left: 16px;
  }
  .field .chevron { position: absolute; right: 14px; top: 15px; }
  .submit-btn {
    height: 50px; background: var(--navy); color: var(--white);
    font-size: 20px; line-height: 50px; text-align: center;
  }
  .privacy-note { margin: 30px 0 0 6px; font-size: 15px; line-height: 19px; width: 430px; }
  .photo { position: absolute; left: 650px; width: 250px; border: 1px solid #9a9a9a; }
  .photo.lounge { top: 167px; height: 237px; background: linear-gradient(180deg, #d9e4ea 0%, #a9a39a 45%, var(--photo-warm) 100%); }
  .photo.kitchen { top: 426px; height: 249px; background: linear-gradient(180deg, #e2d7c4 0%, var(--photo-cool) 50%, #7a5a45 100%); }
  .photo.copy-room { top: 694px; height: 251px; background: linear-gradient(180deg, #ece6cf 0%, var(--photo-light) 55%, #a89b80 100%); }
  .site-footer {
    position: absolute; left: 0; top: 979px; width: 1000px; height: 233px;
    background: var(--navy); color: var(--white);
  }
  .footer-heading { position: absolute; top: 22px; font-size: 24px; font-weight: 400; }
  .quick-links-heading { left: 99px; }
  .contact-heading { left: 650px; }
  .link-column { position: absolute; top: 58px; list-style: none; font-size: 16px; line-height: 20px; }
  .link-column.first { left: 99px; }
  .link-column.second { left: 373px; }
  .link-column .current { color: var(--accent); }
  .mini-form { position: absolute; left: 650px; top: 62px; width: 250px; }
  .mini-input {
    height: 30px; background: var(--white); color: var(--navy);
    font-size: 15px; line-height: 30px; padding-left: 13px; margin-bottom: 4px;
  }
  .mini-input + .mini-input { height: 28px; line-height: 28px; margin-bottom: 2px; }
  .mini-submit { height: 28px; background: var(--accent); color: var(--navy); text-align: center; font-size: 15px; line-height: 28px; }
  .copyright { position: absolute; left: 99px; top: 183px; font-size: 14px; }
  .social { position: absolute; left: 825px; top: 177px; display: flex; gap: 6px; }
  .social span { width: 20px; height: 20px; border-radius: 50%; background: var(--white); }
</style>
</head>
<body>
<div class="page">
  <header class="brand">
    <span class="brand-rule left"></span>
    <span class="brand-name">Calloway</span>
    <span class="brand-rule right"></span>
  </header>
  <h1 class="page-title">Request more information</h1>

  <form class="request-form">
    <div class="field">First Name</div>
    <div class="field">Last Name</div>
    <div class="field">Company Name</div>
    <div class="field">Phone Number</div>
    <div class="field">Email</div>
    <div class="field">Property interested in
      <svg class="chevron" width="22" height="18" viewBox="0 0 22 18"><path d="M1 3 L11 15 L21 3" fill="none" stroke="#000" stroke-width="4"/></svg>
    </div>
    <div class="field">Product interested in
      <svg class="chevron" width="22" height="18" viewBox="0 0 22 18"><path d="M1 3 L11 15 L21 3" fill="none" stroke="#000" stroke-width="4"/></svg>
    </div>
    <div class="field">Request a tour</div>
    <div class="field">Number of people</div>
    <div class="field">Move-in date</div>
    <div class="submit-btn">Submit</div>
    <p class="privacy-note">* We take your privacy very seriously &amp; will not share your information to anyone</p>
  </form>

  <div class="photo lounge" role="img" aria-label="Office lounge with wood floor and white seating"></div>
  <div class="photo kitchen" role="img" aria-label="Break area with counter, stools and vending machine"></div>
  <div class="photo copy-room" role="img" aria-label="Copy room with mailboxes, copier and wall screen"></div>

  <footer class="site-footer">
    <h2 class="footer-heading quick-links-heading">Quick Links</h2>
    <ul class="link-column first">
      <li class="current">Home</li>
      <li>About us</li>
      <li>Contact us</li>
      <li>Testimonials</li>
      <li>FAQ</li>
    </ul>
    <ul class="link-column second">
      <li>Careers</li>
      <li>Furniture</li>
      <li>Specials</li>
      <li>Sitemap</li>
      <li>Privacy policy</li>
    </ul>
    <h2 class="footer-heading contact-heading">Quick Contact Form</h2>
    <div class="mini-form">
      <div class="mini-input">Name</div>
      <div class="mini-input">Email</div>
      <div class="mini-submit">Submit</div>
    </div>
    <p class="copyright">Copyright 2016 Calloway Business Centers - All Rights Reserved</p>
    <div class="social" aria-label="Social links"><span></span><span></span><span></span></div>
  </footer>
</div>
</body>
</html>
```